Need a design for Loan Site with new age design

We need a design for our site www.credvista.in , we deal with different verticals like home loan, personal loan, loan against property and business loans. Feel free to get in touch if you have any questions.

I have like the concept of the drop down on the eye level where consumer is able to select the product they wish and continue with the form https://www.tulsiorbit.com/ . They are in the same line of business as we are.

Here are few more designs which i personally like just to get idea about the taste

https://plumridgestudio.com/
http://zenpik.com/partners

Industry/Entity Type

Loan

Number of Pages Required

2 page

Colors
34a7d7
add136
faa54b
fbee3e

Requirements
Must have
• I have like the concept of the drop down on the eye level where consumer is able to select the product they wish and continue with the form https://www.tulsiorbit.com/ . They are in the same line of business as we are.
• Here are few more designs which i personally like just to get idea about the taste
• https://plumridgestudio.com/
• http://zenpik.com/partners

```html
<!DOCTYPE html>
<html lang="en">
<head>
<meta charset="utf-8">
<title>CredVista – Compare Loan Rates</title>
<link href="https://fonts.googleapis.com/css2?family=Lato:wght@300;400;700&display=swap" rel="stylesheet">
<style>
:root{
  --sky:#34a7d7;
  --lime:#add136;
  --orange:#faa54b;
  --sun:#fbee3e;
  --brand-blue:#0a7cc4;
  --heading-blue:#1d5d99;
  --ink:#222;
  --ink-dark:#1f2a36;
  --muted:#666;
  --field:#efefef;
  --hero-a:#dcd9c3;
  --hero-b:#cdc8ac;
  --white:#fff;
  --rule:rgba(255,255,255,.55);
}
*{box-sizing:border-box;margin:0;padding:0}
html,body{width:1200px;height:2400px;overflow:hidden}
body{font-family:'Lato',sans-serif;color:var(--ink);background:var(--white);position:relative}

/* Hero */
.hero{position:absolute;left:0;top:0;width:1200px;height:587px;overflow:hidden}
.hero-bg{position:absolute;inset:0;background:linear-gradient(90deg,var(--hero-a) 0%,#d6d2b9 55%,var(--hero-b) 100%)}
.hero-portrait{position:absolute;right:0;top:0;width:400px;height:587px;background:radial-gradient(ellipse 55% 60% at 62% 55%,rgba(120,90,70,.45) 0%,rgba(236,230,220,.45) 55%,rgba(205,200,172,0) 100%)}
.site-header{position:absolute;left:171px;top:56px;width:626px;height:75px;background:var(--white);display:flex;align-items:center;justify-content:space-between;padding:0 16px 0 14px}
.brand{display:flex;align-items:center;gap:10px;color:var(--heading-blue);font-weight:700;font-size:20px}
.brand-mark{width:28px;height:28px;border-radius:50%;background:var(--lime)}
.header-nav{font-size:14px;line-height:25px;color:#444}
.search-panel{position:absolute;left:805px;top:51px;width:224px;height:80px;background:rgba(255,255,255,.55);padding:23px 14px}
.search-box{height:33px;background:var(--white);border:1px solid #ccc;display:flex;align-items:center;justify-content:space-between;padding:0 8px;font-size:11px;color:#888}
.hero-title{position:absolute;left:171px;top:180px;font-size:32px;line-height:40px;color:var(--heading-blue);font-weight:400}
.hero-title strong{font-weight:700}
.hero-sub{position:absolute;left:173px;top:235px;font-size:20px;line-height:26px;color:#111}
.hero-sub::after{content:"";display:block;width:60px;height:4px;margin-top:6px;background:var(--sun)}
.quote-form{position:absolute;left:171px;top:280px;width:439px;height:307px;background:var(--white);padding:16px 16px;box-shadow:0 14px 14px -8px rgba(0,0,0,.35);border-top:4px solid var(--lime)}
.field{height:35px;background:var(--field);margin-bottom:11px;display:flex;align-items:center;justify-content:space-between;padding:0 11px;font-size:12px;color:#777}
.form-foot{display:flex;align-items:center;gap:30px;margin-top:14px}
.cta-btn{width:187px;height:43px;background:var(--orange);color:var(--ink-dark);font-size:12px;font-weight:700;display:flex;align-items:center;justify-content:center;gap:10px;border-radius:3px}
.privacy-note{font-size:10px;color:#888;line-height:14px}

/* Partners */
.partners{position:absolute;left:0;top:587px;width:1200px;height:447px;text-align:center}
.partners-kicker{position:absolute;top:110px;width:100%;font-size:38px;line-height:46px;font-weight:300;color:#555}
.partners-title{position:absolute;top:163px;width:100%;font-size:40px;line-height:46px;font-weight:400;color:#555}
.partners-title::after{content:"";display:block;width:80px;height:4px;margin:14px auto 0;background:linear-gradient(90deg,var(--lime),var(--sun),var(--orange))}
.partner-row{position:absolute;left:171px;top:296px;width:858px;display:flex;justify-content:space-between;align-items:center}
.partner{display:flex;align-items:center;gap:7px;font-size:16px;font-weight:700}
.partner i{display:block;width:16px;height:16px}
.p1{color:#9b1b4a}.p1 i{background:#9b1b4a}
.p2{color:#1b5aa8}.p2 i{background:#1b5aa8;border-radius:50%}
.p3{color:#c0261f}.p3 i{background:#c0261f;width:24px;height:24px}
.p4{color:#9e1d20}.p4 i{background:#9e1d20;border-radius:50%}
.p5{color:#8a1a22}
.p6{color:#1c3d7a}.p6 i{background:#1c3d7a;border-radius:50%}

/* Features */
.features{position:absolute;left:0;top:1034px;width:1200px;height:592px;display:flex}
.features-panel{width:648px;background:linear-gradient(160deg,var(--brand-blue) 0%,var(--sky) 100%);position:relative;color:var(--white)}
.features-title{position:absolute;left:171px;top:74px;font-size:38px;line-height:46px;font-weight:700}
.features-title::after{content:"";display:block;width:56px;height:4px;margin-top:8px;background:var(--sun)}
.feature-item{position:absolute;left:171px;display:flex;align-items:center;gap:10px;font-size:18px;line-height:22px}
.rule-dashed{position:absolute;left:141px;width:155px;border-top:1px dashed var(--rule)}
.rule-solid{position:absolute;left:296px;width:352px;border-top:1px solid var(--rule)}
.features-photo{flex:1;background:linear-gradient(135deg,#8c6a4e 0%,#d9d7cf 40%,#5c7fa8 70%,#24344f 100%)}

/* Subscribe */
.subscribe{position:absolute;left:0;top:1626px;width:1200px;height:294px;text-align:center}
.subscribe-title{position:absolute;top:72px;width:100%;font-size:38px;line-height:46px;font-weight:300;color:#444}
.subscribe-sub{position:absolute;top:142px;width:100%;font-size:17px;line-height:22px;color:#555;font-weight:300}
.subscribe-form{position:absolute;left:298px;top:172px;display:flex}
.subscribe-input{width:444px;height:45px;background:var(--field);border:1px solid #ddd}
.subscribe-btn{width:162px;height:45px;background:var(--lime);color:var(--ink-dark);font-size:21px;display:flex;align-items:center;justify-content:center}

/* Call to action */
.cta-band{position:absolute;left:0;top:1920px;width:1200px;height:358px;background:linear-gradient(100deg,var(--brand-blue) 0%,var(--sky) 55%,#1f78c0 100%);text-align:center}
.cta-title{position:absolute;top:104px;width:100%;font-size:35px;line-height:42px;font-weight:300;color:var(--white)}
.inquire-btn{position:absolute;left:480px;top:187px;width:240px;height:56px;background:var(--sun);border-bottom:3px solid var(--orange);font-size:21px;color:var(--ink-dark);display:flex;align-items:center;justify-content:center}

/* Footer */
.site-footer{position:absolute;left:0;top:2278px;width:1200px;height:122px;text-align:center}
.social-links{position:absolute;top:32px;width:100%;display:flex;justify-content:center;gap:20px;font-size:13px;line-height:16px;color:var(--heading-blue)}
.social-links span{display:flex;align-items:center;gap:5px}
.social-links i{display:block;width:8px;height:8px;border-radius:50%;background:var(--lime)}
.copyright{position:absolute;top:74px;width:100%;font-size:12px;line-height:16px;color:#888}
</style>
</head>
<body>

<section class="hero">
  <div class="hero-bg" role="img" aria-label="Soft beige textured backdrop"></div>
  <div class="hero-portrait" role="img" aria-label="Graduate in cap and glasses thinking"></div>

  <header class="site-header">
    <div class="brand"><span class="brand-mark"></span>CredVista</div>
    <nav class="header-nav">
      <div>Compare Loan Rates</div>
      <div>Secured / Unsecured Loans</div>
    </nav>
  </header>
  <div class="search-panel">
    <div class="search-box">Search...
      <svg width="14" height="14" viewBox="0 0 14 14"><circle cx="6" cy="6" r="4.5" fill="none" stroke="#777" stroke-width="1.4"/><line x1="9.3" y1="9.3" x2="13" y2="13" stroke="#777" stroke-width="1.4"/></svg>
    </div>
  </div>

  <h1 class="hero-title">Looking For a <strong>SECURED OR UNSECURED</strong> Loan ?</h1>
  <p class="hero-sub">We will help you get Best Interest Rate</p>

  <form class="quote-form">
    <div class="field">Loan Amount<svg width="10" height="6" viewBox="0 0 10 6"><path d="M1 1l4 4 4-4" fill="none" stroke="#555" stroke-width="1.5"/></svg></div>
    <div class="field">Loan Type<svg width="10" height="6" viewBox="0 0 10 6"><path d="M1 1l4 4 4-4" fill="none" stroke="#555" stroke-width="1.5"/></svg></div>
    <div class="field">Full Name</div>
    <div class="field">Phone</div>
    <div class="field">Email</div>
    <div class="form-foot">
      <div class="cta-btn">COMPARE RATES NOW<svg width="7" height="11" viewBox="0 0 7 11"><path d="M1 1l4.5 4.5L1 10" fill="none" stroke="#1f2a36" stroke-width="1.6"/></svg></div>
      <div class="privacy-note">We are against spam<br>and we respect your privacy</div>
    </div>
  </form>
</section>

<section class="partners">
  <h2 class="partners-kicker">We work with</h2>
  <p class="partners-title">ALL PREMIUM FINANCIAL INSTITUTIONS</p>
  <div class="partner-row">
    <span class="partner p1"><i></i>Arvel Bank</span>
    <span class="partner p2"><i></i>Kesar Finserv</span>
    <span class="partner p3"><i></i>Suryadeep Finance</span>
    <span class="partner p4"><i></i>Indrapath Bank</span>
    <span class="partner p5">Sindhuvan Bank</span>
    <span class="partner p6"><i></i>Koshal Bank</span>
  </div>
</section>

<section class="features">
  <div class="features-panel">
    <h2 class="features-title">OUR FEATURES</h2>
    <div class="feature-item" style="top:179px"><svg width="20" height="20" viewBox="0 0 20 20"><circle cx="10" cy="10" r="9" fill="#add136"/><path d="M5.5 10.5l3 3 6-6.5" fill="none" stroke="#fff" stroke-width="2"/></svg>Doorstep Deliveries</div>
    <div class="rule-dashed" style="top:246px"></div><div class="rule-solid" style="top:246px"></div>
    <div class="feature-item" style="top:291px"><svg width="20" height="20" viewBox="0 0 20 20"><circle cx="10" cy="10" r="9" fill="#add136"/><path d="M5.5 10.5l3 3 6-6.5" fill="none" stroke="#fff" stroke-width="2"/></svg>Easy Documentation</div>
    <div class="rule-solid" style="top:358px"></div>
    <div class="feature-item" style="top:403px"><svg width="20" height="20" viewBox="0 0 20 20"><circle cx="10" cy="10" r="9" fill="#add136"/><path d="M5.5 10.5l3 3 6-6.5" fill="none" stroke="#fff" stroke-width="2"/></svg>Get Approval within 7 business days</div>
    <div class="rule-dashed" style="top:475px"></div><div class="rule-solid" style="top:475px"></div>
    <div class="feature-item" style="top:523px"><svg width="20" height="20" viewBox="0 0 20 20"><circle cx="10" cy="10" r="9" fill="#add136"/><path d="M5.5 10.5l3 3 6-6.5" fill="none" stroke="#fff" stroke-width="2"/></svg>Compare Quote from all major financial institutions</div>
  </div>
  <div class="features-photo" role="img" aria-label="Person filling in a loan application form at a wooden desk with coffee and notebooks"></div>
</section>

<section class="subscribe">
  <h2 class="subscribe-title">STAY IN TOUCH</h2>
  <p class="subscribe-sub">Subscribe to be the first to know about our great special offers.</p>
  <div class="subscribe-form">
    <div class="subscribe-input"></div>
    <div class="subscribe-btn">Subscribe</div>
  </div>
</section>

<section class="cta-band" role="img" aria-label="Blue-tinted scene of people using phones and tablets over banking figures">
  <h2 class="cta-title">WHAT ARE YOU WAITING FOR?</h2>
  <div class="inquire-btn">INQUIRE NOW</div>
</section>

<footer class="site-footer">
  <div class="social-links">
    <span><i></i>Chirpline</span>
    <span><i></i>Circlebook</span>
    <span><i></i>Vidstream</span>
    <span><i></i>Linkwork</span>
  </div>
  <p class="copyright">© 2016 CredVista . All Rights Reserved</p>
</footer>

</body>
</html>
```